Tallgrove Vale Management

I need a professional website. My current website is tallgrovevalemanagement.com and I hate it. It was created with some AI tool very quickly because I needed a site up and running with no advanced notice. I’m open to all designs .. I trust you, the professionals will deliver the results I’m anxiously awaiting! :)

```html
<!DOCTYPE html>
<html lang="en">
<head>
<meta charset="utf-8">
<title>Tallgrove Vale Management</title>
<link href="https://fonts.googleapis.com/css2?family=Poppins:ital,wght@0,400;0,500;0,600;0,700;0,800;1,400;1,500&display=swap" rel="stylesheet">
<style>
:root{
  --navy:#253559;
  --navy-card:#33466f;
  --red:#b8232f;
  --white:#ffffff;
  --grey-bg:#ececec;
  --text:#333a48;
  --sky:#9fc8ea;
}
*{margin:0;padding:0;box-sizing:border-box}
html,body{width:1200px;height:4060px;overflow:hidden}
body{position:relative;background:var(--white);font-family:"Poppins",sans-serif;color:var(--text)}
.abs{position:absolute}
.brand-name{font-family:"Poppins",sans-serif;font-weight:800;color:var(--navy);letter-spacing:.5px;line-height:1.05}
.btn{position:absolute;display:flex;align-items:center;padding-left:20px;height:44px;background:var(--navy);color:var(--white);font-weight:600;font-size:14px;letter-spacing:.3px;border-left:4px solid var(--red);clip-path:polygon(0 0,88% 0,100% 50%,88% 100%,0 100%)}
.section-title{position:absolute;left:0;width:1200px;text-align:center;font-weight:700;font-size:40px;color:var(--navy);letter-spacing:.3px}
.rule{position:absolute;height:6px;width:160px;background:var(--red)}
.rule.center{left:520px}

/* header */
.site-header{position:absolute;top:0;left:0;width:1200px;height:93px;background:var(--white);z-index:3}
.logo-block{position:absolute;left:120px;top:24px;z-index:4;display:flex;align-items:center;gap:10px}
.logo-block .mark{width:20px;height:20px;background:var(--red)}
.logo-block .brand-name{font-size:20px}
.nav{position:absolute;top:38px;left:450px;display:flex;gap:0}
.nav a{display:block;font-size:14px;font-weight:500;color:var(--navy);text-decoration:none;margin-right:52px;position:relative}
.nav a.active::after{content:"";position:absolute;left:0;right:0;bottom:-12px;height:3px;background:var(--red)}

/* hero */
.hero-photo{position:absolute;top:93px;left:0;width:1200px;height:650px;background:linear-gradient(180deg,#6aaee8 0%,#a9d2f2 35%,#d9d2c3 55%,#7b8f68 80%,#5c7a42 100%)}
.hero-title{position:absolute;right:118px;top:172px;text-align:right;font-weight:800;font-size:47px;line-height:50px;color:var(--navy)}

/* about */
.about-title{position:absolute;left:120px;top:800px;font-weight:700;font-size:40px;line-height:46px;color:var(--navy)}
.about-title .accent{color:var(--red)}
.about-copy{position:absolute;left:120px;top:940px;width:515px;font-size:15px;line-height:22px;color:var(--text)}
.about-copy p+p{margin-top:22px}

/* services */
.services-title{color:var(--white);top:1475px}
.service-card{position:absolute;top:1585px;width:218px;height:247px;background:var(--navy-card);border-radius:8px;padding:22px 22px 0 23px;color:var(--white)}
.service-card svg.icon{width:54px;height:54px}
.service-card h3{font-size:16px;font-weight:600;margin-top:20px;letter-spacing:.2px}
.service-card p{font-size:13px;line-height:16px;margin-top:8px;color:#e6e9f0}
.service-card .plus{position:absolute;right:0;bottom:0;width:32px;height:32px;background:var(--red);border-radius:5px 0 5px 0;display:flex;align-items:center;justify-content:center}

/* property */
.property-card{position:absolute;top:2166px;width:289px}
.property-card .photo{width:289px;height:190px;border-radius:12px}
.property-card h3{font-size:17.5px;line-height:22px;font-weight:700;color:var(--navy);margin-top:22px}
.property-card p{font-size:14px;line-height:17px;color:var(--text);margin-top:20px}
.property-card a{display:inline-block;margin-top:17px;font-size:14px;font-weight:600;color:var(--navy);text-decoration:underline}

/* expertise */
.expertise-photo{position:absolute;left:0;top:2646px;width:553px;height:394px;border-radius:0 34px 34px 0;background:linear-gradient(120deg,#8a5e3c 0%,#c79b74 40%,#2d3c5c 70%,#1f2a42 100%)}
.expertise-title{position:absolute;left:598px;top:2672px;font-weight:700;font-size:40px;line-height:44px;color:var(--navy)}
.expertise-copy{position:absolute;left:600px;top:2846px;width:430px;font-size:15px;line-height:22px;color:var(--navy)}

/* testimonials */
.testimonials-bg{position:absolute;left:0;top:3098px;width:1200px;height:460px;background:var(--grey-bg)}
.avatar{position:absolute;left:268px;top:3348px;width:156px;height:156px;border-radius:50%;border:5px solid var(--red);background:linear-gradient(160deg,#c9b39a,#3b4a4a)}
.stars{position:absolute;left:458px;top:3340px;color:var(--red);font-size:24px;letter-spacing:2px}
.quote{position:absolute;left:456px;top:3376px;width:540px;font-style:italic;font-size:16px;line-height:23px;color:var(--navy)}
.quote-name{position:absolute;left:456px;top:3478px;font-weight:700;font-size:14px;color:var(--navy)}

/* footer */
.footer-logo{position:absolute;left:120px;top:3812px;display:flex;align-items:center;gap:10px}
.footer-logo .mark{width:22px;height:22px;background:var(--red)}
.footer-logo .brand-name{color:var(--white);font-size:22px}
.footer-col{position:absolute;top:3760px;color:var(--white)}
.footer-col h4{font-size:19px;font-weight:500;letter-spacing:.3px;margin-bottom:16px}
.footer-col ul{list-style:none}
.footer-col li{font-size:15px;line-height:28px}
.divider{position:absolute;top:3748px;width:1px;height:200px;background:#4b5b80}
.contact-row{display:flex;gap:20px;align-items:flex-start;font-size:15px;line-height:19px;margin-bottom:16px}
.footer-bottom{position:absolute;top:4004px;left:120px;width:960px;display:flex;justify-content:space-between;color:var(--white);font-size:14px}
</style>
</head>
<body>

<header class="site-header">
  <nav class="nav">
    <a class="active">HOME</a>
    <a>SERVICES</a>
    <a>ABOUT</a>
    <a>CONTACT</a>
  </nav>
  <div class="btn" style="left:932px;top:28px;width:150px">GET A QUOTE</div>
</header>
<div class="logo-block"><span class="mark"></span><span class="brand-name">TALLGROVE<br>VALE</span></div>

<!-- hero -->
<div class="hero-photo" role="img" aria-label="Row of suburban two-storey houses with trees under a blue sky"></div>
<svg class="abs" style="left:0;top:500px" width="1200" height="260" viewBox="0 0 1200 260">
  <polygon points="0,20 600,242 1200,20 1200,260 0,260" fill="#fff"/>
  <polygon points="100,64 600,240 1100,58 1100,62 600,250 100,70" fill="var(--red)"/>
  <polygon points="100,64 600,230 1100,56 600,242" fill="var(--red)"/>
</svg>
<h1 class="hero-title">A TRUE PARTNER,<br>NOT JUST A VENDOR.</h1>
<div class="btn" style="left:932px;top:288px;width:150px">GET A QUOTE</div>

<!-- about -->
<h2 class="about-title">ABOUT <span class="accent">TALLGROVE VALE</span><br>MANAGEMENT</h2>
<div class="rule" style="left:120px;top:912px"></div>
<div class="about-copy">
  <p>Our organization delivers comprehensive property management solutions that optimize asset performance and tenant satisfaction. By integrating advanced analytics with proven operational frameworks, our specialists ensure each property achieves sustained value appreciation.</p>
  <p>Drawing on decades of collective expertise, the team facilitates regulatory compliance, cost efficiency, and proactive maintenance. This disciplined approach enables owners to preserve capital, enhance occupancy rates, and demonstrate long-term resilience across diverse market conditions.</p>
</div>
<div class="btn" style="left:120px;top:1196px;width:150px">GET A QUOTE</div>

<svg class="abs" style="left:664px;top:775px" width="436" height="500" viewBox="0 0 436 500">
  <defs>
    <linearGradient id="hexPhoto" x1="0" y1="0" x2="1" y2="1">
      <stop offset="0" stop-color="#7d7f86"/>
      <stop offset=".55" stop-color="#b9a68a"/>
      <stop offset="1" stop-color="#e7e3dc"/>
    </linearGradient>
  </defs>
  <polygon points="218,2 434,126 434,374 218,498 2,374 2,126" fill="var(--red)"/>
  <polygon points="218,18 420,134 420,366 218,482 16,366 16,134" fill="#fff"/>
  <polygon points="218,30 410,140 410,360 218,470 26,360 26,140" fill="var(--navy)"/>
  <polygon points="218,46 396,148 396,352 218,454 40,352 40,148" fill="url(#hexPhoto)" role="img" aria-label="Hand stacking coins beside a small model house"/>
</svg>

<!-- services -->
<svg class="abs" style="left:0;top:1310px" width="1200" height="652" viewBox="0 0 1200 652">
  <polygon points="0,228 600,50 1200,228 1200,652 0,652" fill="var(--navy)"/>
  <polygon points="100,186 600,4 1100,186 600,22" fill="var(--red)"/>
</svg>
<h2 class="section-title services-title">OUR SERVICES</h2>
<div class="rule center" style="top:1543px"></div>

<div class="service-card" style="left:120px">
  <svg class="icon" viewBox="0 0 54 54" fill="none" stroke="#fff" stroke-width="1.8"><path d="M10 26 27 10l17 16"/><path d="M15 22v14h24V22"/><rect x="23" y="26" width="8" height="10"/><path d="M4 44h14l10 4 18-6"/></svg>
  <h3>SERVICE NAME</h3>
  <p>Lorem ipsum dolor sitlosg amet, consectetur adjelrs ipiscing elit, sed do eiuloe sm od tempor incidid lore unt ut labore et.</p>
  <div class="plus"><svg width="14" height="14" viewBox="0 0 14 14"><path d="M7 1v12M1 7h12" stroke="#fff" stroke-width="3"/></svg></div>
</div>
<div class="service-card" style="left:369px">
  <svg class="icon" viewBox="0 0 54 54" fill="none" stroke="#fff" stroke-width="1.8"><rect x="6" y="12" width="16" height="36"/><rect x="22" y="6" width="14" height="42"/><rect x="36" y="22" width="12" height="26"/><path d="M10 18h8M10 26h8M10 34h8M26 14h6M26 22h6M26 30h6M40 28h4M40 36h4M2 48h50"/></svg>
  <h3>SERVICE NAME</h3>
  <p>Lorem ipsum dolor sitlosg amet, consectetur adjelrs ipiscing elit, sed do eiuloe sm od tempor incidid lore unt ut labore et.</p>
  <div class="plus"><svg width="14" height="14" viewBox="0 0 14 14"><path d="M7 1v12M1 7h12" stroke="#fff" stroke-width="3"/></svg></div>
</div>
<div class="service-card" style="left:614px">
  <svg class="icon" viewBox="0 0 54 54" fill="none" stroke="#fff" stroke-width="1.8"><circle cx="22" cy="12" r="8"/><path d="M18 20 8 44l4 4 4-6 3 2 3-10"/><path d="M26 36l13-12 13 12"/><path d="M30 33v15h18V33"/><rect x="36" y="38" width="6" height="10"/></svg>
  <h3>SERVICE NAME</h3>
  <p>Lorem ipsum dolor sitlosg amet, consectetur adjelrs ipiscing elit, sed do eiuloe sm od tempor incidid lore unt ut labore et.</p>
  <div class="plus"><svg width="14" height="14" viewBox="0 0 14 14"><path d="M7 1v12M1 7h12" stroke="#fff" stroke-width="3"/></svg></div>
</div>
<div class="service-card" style="left:862px">
  <svg class="icon" viewBox="0 0 54 54" fill="none" stroke="#fff" stroke-width="1.8"><path d="M8 6h24l8 8v30H8z"/><path d="M14 24 24 15l10 9"/><path d="M17 22v10h14V22"/><path d="M14 38h12"/><path d="M48 20 30 42l-4 6 6-3 18-22z"/></svg>
  <h3>SERVICE NAME</h3>
  <p>Lorem ipsum dolor sitlosg amet, consectetur adjelrs ipiscing elit, sed do eiuloe sm od tempor incidid lore unt ut labore et.</p>
  <div class="plus"><svg width="14" height="14" viewBox="0 0 14 14"><path d="M7 1v12M1 7h12" stroke="#fff" stroke-width="3"/></svg></div>
</div>

<!-- property -->
<h2 class="section-title" style="top:2045px">OUR PROPERTY</h2>
<div class="rule center" style="top:2115px"></div>

<div class="property-card" style="left:120px">
  <div class="photo" role="img" aria-label="Modern grey and stone house at dusk" style="background:linear-gradient(180deg,#e6b7c9 0%,#9aa0b3 40%,#4d4f55 75%,#5f7a45 100%)"></div>
  <h3>Lorem ipsum dolor sit amet, conse ctetur adipiscing.</h3>
  <p>Lorem ipsum dolor sit ameone cte tur adipiscing elit, sed do eiu smod tempor incididunt ut lab ore et dol ore magna aliqua.</p>
  <a>Read More</a>
</div>
<div class="property-card" style="left:456px">
  <div class="photo" role="img" aria-label="Large white two-storey house with lit windows at evening" style="background:linear-gradient(180deg,#3f7fd6 0%,#8fb4e0 40%,#cbc3b4 65%,#4f6a3a 100%)"></div>
  <h3>Lorem ipsum dolor sit amet, conse ctetur adipiscing.</h3>
  <p>Lorem ipsum dolor sit ameone cte tur adipiscing elit, sed do eiu smod tempor incididunt ut lab ore et dol ore magna aliqua.</p>
  <a>Read More</a>
</div>
<div class="property-card" style="left:792px">
  <div class="photo" role="img" aria-label="Grey shingled family house with garage doors" style="background:linear-gradient(180deg,#c9dbef 0%,#8e959e 45%,#6d6258 70%,#5b7b3f 100%)"></div>
  <h3>Lorem ipsum dolor sit amet, conse ctetur adipiscing.</h3>
  <p>Lorem ipsum dolor sit ameone cte tur adipiscing elit, sed do eiu smod tempor incididunt ut lab ore et dol ore magna aliqua.</p>
  <a>Read More</a>
</div>

<!-- expertise -->
<div class="expertise-photo" role="img" aria-label="Agent handing house keys across a desk with a small model house"></div>
<h2 class="expertise-title">EXPERTISE<br>ROOTED IN ASSET<br>PRESERVATION</h2>
<div class="rule" style="left:600px;top:2812px"></div>
<p class="expertise-copy">The organization applies rigorously tested frameworks and data-driven methodologies to safeguard property value while elevating tenant experience.</p>
<div class="btn" style="left:600px;top:2936px;width:150px">LEARN MORE</div>

<!-- testimonials -->
<div class="testimonials-bg"></div>
<h2 class="section-title" style="top:3210px">CLIENT TESTIMONIALS</h2>
<div class="rule center" style="top:3280px"></div>
<div class="avatar" role="img" aria-label="Client holding a house key"></div>
<div class="stars">★★★★★</div>
<p class="quote">Lorem ipsum dolor sit amet, consectetur adipiscing elit, sed do eiusmod tempor incididunt ut labore et dolore magna aliqua. Quis ipsum suspendisse ultrices gravida. Risus commodo viverra maecenas accumsan lacus vel facilisis.</p>
<div class="quote-name">-DARA WHITFIELD</div>

<!-- footer -->
<svg class="abs" style="left:0;top:3480px" width="1200" height="580" viewBox="0 0 1200 580">
  <polygon points="0,0 600,218 1200,0 1200,580 0,580" fill="var(--navy)"/>
  <polygon points="60,40 600,228 1140,40 1140,46 600,212 60,46" fill="var(--red)"/>
  <polygon points="60,40 600,202 1140,40 600,228" fill="var(--red)"/>
</svg>
<div class="footer-logo"><span class="mark"></span><span class="brand-name">TALLGROVE<br>VALE</span></div>
<div class="divider" style="left:355px"></div>
<div class="divider" style="left:563px"></div>
<div class="divider" style="left:873px"></div>
<div class="footer-col" style="left:410px">
  <h4>LINKS</h4>
  <ul><li>Home</li><li>Services</li><li>About</li><li>Contact</li></ul>
</div>
<div class="footer-col" style="left:615px">
  <h4>CONTACT</h4>
  <div class="contact-row">
    <svg width="22" height="26" viewBox="0 0 22 26"><path d="M11 1a9 9 0 0 0-9 9c0 7 9 15 9 15s9-8 9-15a9 9 0 0 0-9-9z" fill="#fff"/><circle cx="11" cy="10" r="3.5" fill="var(--navy)"/></svg>
    <span>Location Placeholder<br>Lorem Ipsum343</span>
  </div>
  <div class="contact-row">
    <svg width="24" height="24" viewBox="0 0 24 24"><path d="M5 2l4 1 2 5-3 2a13 13 0 0 0 6 6l2-3 5 2 1 4-3 3C10 22 2 14 2 5z" fill="#fff"/></svg>
    <span>Phone:<br>555 014 2290</span>
  </div>
</div>
<div class="footer-col" style="left:942px">
  <h4>LINKS</h4>
  <ul><li>Service Name 1</li><li>Service Name 2</li><li>Service Name 3</li><li>Service Name 4</li></ul>
</div>
<div class="footer-bottom">
  <span>Tallgrove Vale Management LLC</span>
  <span>info@tallgrovevalemanagement.com</span>
</div>

</body>
</html>
```